Workers comp/Business Ins/ Payroll- Postcard

I own an insurance agency.  I'm interested in getting some professional advice on how to design a message for what i want to sell.  The products I want to sell are 1) Workers compensation 2) business Insurance 3) Payroll processing. They are integrated together but I'm not sure if it's too much to put on a postcard and if I don't put it on a postcard I could be missing out on sales.
I have the ability to look up what Insurance company a business has their workers compensation  policy with, along with their expiration date.  Based on that information I can tell if the business is overpaying for their Workers compensation. insurance. Most companies are overpaying so I can usually save a company money very quickly if I can get in front of them. Some businesses work with a broker such as myself and buy a policy. When it's done this way, the business ESTIMATES his payroll for the year and at the end of the year they have to complete an audit to find out the actual payroll. Based on audit, they will either owe more money if they were low or get money back if they were high. The other way a business buys a workers comp. policy is with their payroll company. The payroll company will place the policy on Pay -as- you -go which means when you pay your employees every week they  will also calculate how much the workers comp premium is for the week and take that amount out of their checking account. This method avoids large down payments, helps with cash flow and should be very accurate at the end of the policy term.  This is by far the best way to do this for the businessowner. My company also has payroll company and we do this for the insured as well. However, most payroll company's such as QRT and Wagelon charge the customer $15 every time they do this so if it's weekly it is another $780 a year.  We also complete the insured's audit for them which is a big headache for the businessowner.
One of our biggest benefits of doing business with our company is we have a  Steady Rate Forever. When you sign up your base price will never increase. Payroll companies are famous for "discounting a new client" only to increase the rate in a few months later. Our service is also superior to the other payroll companies who use overseas service centers. We have staff within our office and we can answer questions quickly. We usually save businesses money on  their Payroll processing but it's not what we focus on- We focus on the Service.
Business Insurance- One of our main companies that we represent is Brindle Insurance. Brindle is very competitive and we usually write business accounts where we save the business owner money but offer superior coverages.
in summary, I'm offering 1) better workers compensation rates 2) Pay as you go workers comp. 3) Steady Rate, audits done for you, and superior customer service with our payroll company 4) savings on their business insurance with superior coverages.
Sometimes when we talk to an insured we may start with just their payroll and later get the WC and business liability. Each account is different and we do not pressure people to make decisions and we do what is right for them.  The biggest takeaway is we take some things off the plate for the businessowner where they can make just one phone call to get what they need done.  Our Website is www.harbor-mutual.example. my email is tomk@harbor-mutual.example if you have any questions.
Thank You
Tom Kessor

Target Market(s)
Small business owners 1-50 employees
Industry/Entity Type
Insurance and Payroll
Font styles to use
Other font styles liked:
- Let designer choose

Colors
Designer to choose colors to be used in the design.
Requirements
Must have
- It shouldn't be boring- needs to stand out- can use 6x11 inch postcard

Nice to have
- I like humor but not a must

Should not have
- Nothing I can think of

```html
<!DOCTYPE html>
<html lang="en">
<head>
<meta charset="utf-8">
<title>Harbor Mutual Postcard</title>
<link href="https://fonts.googleapis.com/css2?family=Libre+Baskerville:wght@700&family=Poppins:wght@400;600;700&family=Oswald:wght@500&display=swap" rel="stylesheet">
<style>
:root{
  --backdrop:#8a8a8a;
  --red:#b3181d;
  --red-deep:#8f2323;
  --red-panel:#932626;
  --ink:#1e1e1e;
  --dark:#242424;
  --gray:#8c8c8c;
  --gray-dark:#6b6b6b;
  --white:#ffffff;
}
*{margin:0;padding:0;box-sizing:border-box}
html,body{width:1040px;height:1200px;overflow:hidden}
body{background:var(--backdrop);font-family:"Poppins",sans-serif;position:relative;color:var(--ink)}
.card{position:absolute;left:87px;width:866px;height:473px;background:var(--white);overflow:hidden;box-shadow:0 8px 18px rgba(0,0,0,.35)}
.card--front{top:99px}
.card--back{top:629px;height:472px}
.abs{position:absolute}

/* front */
.hero-band{left:0;top:0;width:866px;height:187px;background:linear-gradient(90deg,#0b2226 0%,#0e2f33 45%,#164a4d 65%,#3b3a2c 85%,#5a2e22 100%)}
.hero-photo{left:482px;top:0;width:384px;height:187px;background:radial-gradient(circle at 76% 40%,#b2292b 0 14%,transparent 15%),radial-gradient(ellipse at 50% 100%,#8a5a2c 0,transparent 60%),linear-gradient(90deg,rgba(22,74,77,0),rgba(60,50,35,.6))}
.headline{left:45px;top:29px;font-family:"Libre Baskerville",serif;font-weight:700;font-size:33px;line-height:33px;color:var(--white);letter-spacing:-.5px}
.headline em{font-style:normal;color:var(--red)}
.tabs{left:43px;top:141px;display:flex;border:2px solid #cfcfcf}
.tab{width:146px;height:76px;background:var(--gray);display:flex;align-items:center;gap:8px;padding-left:10px;color:var(--white);font-weight:600;font-size:12px;line-height:15px;border-right:2px solid #cfcfcf}
.tab:last-child{border-right:0}
.tab--mid{background:var(--gray-dark)}
.features{font-size:10px;line-height:12px}
.feature{position:absolute;display:flex;align-items:center;gap:8px;width:200px}
.feature b{font-weight:700}
.divider-dash{left:266px;top:242px;height:106px;border-left:1px dashed #888}
.brand{left:42px;top:392px;font-weight:600;font-size:17px;color:#7d2020;display:flex;align-items:center;gap:7px;letter-spacing:1px}
.brand i{display:block;width:13px;height:13px;background:#7d2020}
.cta-pill{left:246px;top:378px;width:239px;height:22px;border-radius:11px;background:var(--red);color:var(--white);font-size:12.5px;text-align:center;line-height:22px;box-shadow:0 2px 3px rgba(0,0,0,.3)}
.cta-pill b{font-weight:700}
.phones{left:250px;top:403px;font-weight:600;font-size:14.5px;display:flex;align-items:center;gap:8px}
.or-dot{width:16px;height:16px;border-radius:50%;background:var(--red);color:var(--white);font-size:9px;font-weight:400;display:flex;align-items:center;justify-content:center}
.web{left:248px;top:423px;font-size:12.5px;letter-spacing:2.2px}
.web b{color:var(--red);font-weight:700}
.why{left:550px;top:180px;width:273px;height:210px;background:var(--red-panel);color:var(--white)}
.why h2{height:38px;background:#8a1f20;font-family:"Libre Baskerville",serif;font-size:15px;line-height:38px;padding-left:22px}
.why-item{position:absolute;left:24px;width:235px;display:flex;gap:6px;font-size:11px;line-height:14px}
.why-item b{font-weight:700}
.why-rule{position:absolute;left:20px;width:240px;border-top:1px solid rgba(255,255,255,.35)}
.consult{left:550px;top:390px;width:273px;height:46px;display:flex}
.consult-label{width:165px;background:var(--gray);color:var(--white);font-family:"Oswald",sans-serif;font-size:20px;line-height:46px;text-align:center}
.consult-note{flex:1;background:#8a1f20;color:var(--white);font-weight:700;font-size:10px;line-height:12px;padding:10px 0 0 8px}

/* back */
.back-dark{left:0;top:0;width:552px;height:472px;background:var(--dark)}
.back-band{left:552px;top:99px;width:314px;height:137px;background:var(--dark)}
.back-head{left:44px;top:34px;width:335px;font-family:"Libre Baskerville",serif;font-weight:700;font-size:16.5px;line-height:20px;color:var(--white);letter-spacing:-.6px;white-space:nowrap}
.back-head span{color:var(--red)}
.intro{left:390px;top:34px;width:155px;font-size:10px;line-height:13px;color:var(--white)}
.intro b{font-weight:600}
.cell{position:absolute;width:162px;height:113px}
.cell--photo{background:linear-gradient(135deg,#a52a2d,#8a1e22);color:var(--white);font-weight:700;font-size:12px;line-height:15px;display:flex;align-items:center;justify-content:center;text-align:center}
.cell--list{background:var(--gray);color:var(--white);padding:10px 8px 0 10px;font-size:8px;line-height:10px}
.cell--list li{list-style:none;position:relative;padding-left:10px;margin-bottom:3px}
.cell--list li::before{content:"";position:absolute;left:0;top:2px;width:6px;height:6px;border-radius:50%;background:var(--red)}
.cell--list b{font-weight:700}
.photo{position:absolute;top:112px;width:111px;height:113px}
.quote{left:752px;top:122px;width:100px;font-size:10.5px;line-height:13px;color:var(--white)}
.quote b{font-weight:700}
.rule-light{left:390px;width:145px;border-top:1px solid #666}
.one-call{left:390px;top:258px;width:160px;font-weight:700;font-size:10.5px;line-height:13px;color:var(--white)}
.one-call span{color:var(--red)}
.juggle{left:390px;top:315px;width:150px;font-size:9.5px;line-height:12px;color:var(--white)}
.back-contact{left:392px;color:var(--white);display:flex;align-items:center;gap:4px;white-space:nowrap}
.back-contact--phone{font-weight:700;font-size:13.5px}
.back-contact--email{font-size:8.5px}
.back-web{left:391px;top:430px;font-size:9px;letter-spacing:.5px;color:var(--white);white-space:nowrap}
.back-web b{font-weight:700}
.or-badge{left:502px;top:363px;width:16px;height:16px;border-radius:50%;background:var(--red);color:var(--white);font-size:8px;display:flex;align-items:center;justify-content:center}
</style>
</head>
<body>

<section class="card card--front">
  <div class="abs hero-band"></div>
  <div class="abs hero-photo" role="img" aria-label="Red alarm clock and a seedling growing from coins"></div>
  <h1 class="abs headline">SAVE <em>TIME</em><br>SAVE <em>MONEY</em><br>GAIN <em>PEACE OF MIND</em></h1>

  <div class="abs tabs">
    <div class="tab"><svg width="26" height="26" viewBox="0 0 26 26"><circle cx="13" cy="15" r="9" fill="#e8a93a"/><text x="13" y="19" font-size="11" text-anchor="middle" fill="#5a3a0a" font-family="Poppins">$</text></svg>Workers<br>compensation</div>
    <div class="tab tab--mid"><svg width="26" height="26" viewBox="0 0 26 26"><path d="M13 2 L22 6 V13 C22 19 13 24 13 24 C13 24 4 19 4 13 V6 Z" fill="#f2c94c" stroke="#1f4b8f" stroke-width="2"/><path d="M9 13 L12 16 L17 10" stroke="#1f4b8f" stroke-width="2" fill="none"/></svg>Business<br>Insurance</div>
    <div class="tab"><svg width="26" height="26" viewBox="0 0 26 26"><circle cx="13" cy="13" r="11" fill="#fff" stroke="#e8a93a" stroke-width="3"/><path d="M13 6 V13 L17 15" stroke="#333" stroke-width="2" fill="none"/></svg>Payroll<br>Solutions</div>
  </div>

  <div class="features">
    <div class="feature" style="left:41px;top:240px"><svg width="33" height="33" viewBox="0 0 33 33"><circle cx="16.5" cy="16.5" r="15.5" fill="#a32024" stroke="#d9d9d9" stroke-width="2"/><circle cx="16.5" cy="16.5" r="12" fill="none" stroke="#fff"/></svg><span>Lower Your Workers<br><b>Compensation Costs</b></span></div>
    <div class="feature" style="left:41px;top:278px"><svg width="33" height="33" viewBox="0 0 33 33"><circle cx="16.5" cy="16.5" r="15.5" fill="#5f5f5f" stroke="#d9d9d9" stroke-width="2"/><circle cx="16.5" cy="16.5" r="12" fill="none" stroke="#fff"/></svg><span>Easy "Pay-As-You-Go" Workers<br>Comp — <b>No Big Deposits</b></span></div>
    <div class="feature" style="left:41px;top:316px"><svg width="33" height="33" viewBox="0 0 33 33"><circle cx="16.5" cy="16.5" r="15.5" fill="#a32024" stroke="#d9d9d9" stroke-width="2"/><circle cx="16.5" cy="16.5" r="12" fill="none" stroke="#fff"/></svg><span>Business Insurance That Covers<br>More — <b>For Less</b></span></div>
    <div class="abs divider-dash"></div>
    <div class="feature" style="left:291px;top:240px"><svg width="33" height="33" viewBox="0 0 33 33"><circle cx="16.5" cy="16.5" r="15.5" fill="#a32024" stroke="#d9d9d9" stroke-width="2"/><circle cx="16.5" cy="16.5" r="12" fill="none" stroke="#fff"/></svg><span>Payroll Processing with<br><b>Lifetime Steady Rate</b></span></div>
    <div class="feature" style="left:291px;top:278px"><svg width="33" height="33" viewBox="0 0 33 33"><circle cx="16.5" cy="16.5" r="15.5" fill="#5f5f5f" stroke="#d9d9d9" stroke-width="2"/><circle cx="16.5" cy="16.5" r="12" fill="none" stroke="#fff"/></svg><span>Audits Handled FOR You — <b>No<br>More Headaches</b></span></div>
    <div class="feature" style="left:291px;top:316px"><svg width="33" height="33" viewBox="0 0 33 33"><circle cx="16.5" cy="16.5" r="15.5" fill="#a32024" stroke="#d9d9d9" stroke-width="2"/><circle cx="16.5" cy="16.5" r="12" fill="none" stroke="#fff"/></svg><span>Dedicated U.S.-Based Support<br>Team — <b>No Call Centers!</b></span></div>
  </div>

  <div class="abs brand"><i></i>HARBOR MUTUAL</div>
  <div class="abs cta-pill"><b>CALL US TODAY</b> OR VISIT ONLINE!</div>
  <div class="abs phones">555.010.4821 <span class="or-dot">or</span> (800) 555-0142</div>
  <div class="abs web">www.<b>harbor-mutual</b>.example</div>

  <div class="abs why">
    <h2>Why Choose Harbor Mutual?</h2>
    <div class="why-item" style="top:58px"><svg width="11" height="11" viewBox="0 0 12 12"><circle cx="6" cy="6" r="6" fill="#fff"/><path d="M3 6 L5 8 L9 4" stroke="#932626" stroke-width="1.6" fill="none"/></svg><span><b>Save thousands annually</b> on Workers Comp &amp; Payroll</span></div>
    <div class="why-rule" style="top:93px"></div>
    <div class="why-item" style="top:113px"><svg width="11" height="11" viewBox="0 0 12 12"><circle cx="6" cy="6" r="6" fill="#fff"/><path d="M3 6 L5 8 L9 4" stroke="#932626" stroke-width="1.6" fill="none"/></svg><span>Never deal with <b>mid-year payroll</b> price increases again</span></div>
    <div class="why-rule" style="top:149px"></div>
    <div class="why-item" style="top:169px"><svg width="11" height="11" viewBox="0 0 12 12"><circle cx="6" cy="6" r="6" fill="#fff"/><path d="M3 6 L5 8 L9 4" stroke="#932626" stroke-width="1.6" fill="none"/></svg><span><b>Real humans. Real service. Real savings.</b></span></div>
  </div>
  <div class="abs consult">
    <div class="consult-label">FREE CONSULTATION</div>
    <div class="consult-note">Let's See What You Could Save!</div>
  </div>
</section>

<section class="card card--back">
  <div class="abs back-dark"></div>
  <div class="abs back-band"></div>
  <h2 class="abs back-head"><span>YOUR BUSINESS DESERVES MORE</span><br>THAN COOKIE-CUTTER SERVICE</h2>
  <p class="abs intro"><b>Let Harbor Mutual Simplify<br>Your Insurance &amp; Payroll</b><br>So You Can Focus on<br>Growing Your Business.</p>

  <div class="cell cell--photo" style="left:47px;top:89px" role="img" aria-label="Red-tinted photo of a house">Workers<br>Compensation</div>
  <ul class="cell cell--list" style="left:213px;top:89px">
    <li>We find out if you're overpaying — <b>fast!</b></li>
    <li>Pay-As-You-Go options avoid big audits and cash crunches.</li>
    <li>Most companies are overpaying — <b>we can help fix that!</b></li>
  </ul>
  <ul class="cell cell--list" style="left:47px;top:207px;padding-top:22px">
    <li>Partnered with top carriers like Brindle Insurance</li>
    <li>Superior coverage at highly competitive rates</li>
    <li>Tailored policies — <b>no one-size-fits-all solutions.</b></li>
  </ul>
  <div class="cell cell--photo" style="left:213px;top:207px" role="img" aria-label="Red-tinted photo of insurance paperwork">Business<br>Insurance</div>
  <div class="cell cell--photo" style="left:47px;top:325px" role="img" aria-label="Red-tinted photo of payroll documents">Payroll<br>Processing</div>
  <ul class="cell cell--list" style="left:213px;top:325px;padding-top:8px">
    <li>Lifetime Steady Rate — <b>no hidden hikes.</b></li>
    <li>No extra fees for weekly Workers Comp calculations (unlike QRT/Wagelon!)</li>
    <li>Your payroll audit? Done by us, not by you.</li>
    <li>Fast, responsive U.S.-based support.</li>
  </ul>

  <div class="photo" style="left:390px;background:linear-gradient(180deg,#6f8fb8,#d9cfc0 55%,#5a5e52)" role="img" aria-label="Photo of a home with a red SUV in the driveway"></div>
  <div class="photo" style="left:507px;background:linear-gradient(135deg,#5a6572,#c9ced6 55%,#eef0f2)" role="img" aria-label="Photo of a calculator and financial charts"></div>
  <div class="photo" style="left:623px;background:linear-gradient(135deg,#e8eaec,#9aa3ab 60%,#2e3a4a)" role="img" aria-label="Photo of a business owner working at a laptop"></div>
  <p class="abs quote">We don't pressure. We partner. Every business is different <b>and we do what's right for you."</b></p>

  <div class="abs rule-light" style="top:242px"></div>
  <p class="abs one-call">One Call. One Team.<br>Everything You Need.<br><span>Get Ready to Save Money<br>&amp; Stress Less?</span></p>
  <p class="abs juggle">Stop juggling vendors. Let Harbor Mutual handle it all seamlessly.</p>
  <div class="abs rule-light" style="top:357px"></div>

  <div class="abs back-contact back-contact--phone" style="top:368px"><svg width="12" height="12" viewBox="0 0 12 12"><circle cx="6" cy="6" r="6" fill="#b3181d"/><path d="M3.5 3 L5 3 L5.5 4.5 L4.6 5.2 C5 6.2 5.8 7 6.8 7.4 L7.5 6.5 L9 7 L9 8.5 C6 8.8 3.2 6 3.5 3 Z" fill="#fff"/></svg>555.010.4821</div>
  <div class="abs or-badge">or</div>
  <div class="abs back-contact back-contact--phone" style="top:386px"><svg width="12" height="12" viewBox="0 0 12 12"><circle cx="6" cy="6" r="6" fill="#b3181d"/><path d="M3.5 3 L5 3 L5.5 4.5 L4.6 5.2 C5 6.2 5.8 7 6.8 7.4 L7.5 6.5 L9 7 L9 8.5 C6 8.8 3.2 6 3.5 3 Z" fill="#fff"/></svg>(800) 555-0142</div>
  <div class="abs back-contact back-contact--email" style="top:409px"><svg width="11" height="11" viewBox="0 0 12 12"><circle cx="6" cy="6" r="6" fill="#b3181d"/><rect x="3" y="4" width="6" height="4" fill="none" stroke="#fff" stroke-width=".9"/><path d="M3 4 L6 6.3 L9 4" stroke="#fff" stroke-width=".9" fill="none"/></svg>tomk@harbor-mutual.example</div>
  <div class="abs back-web">www.<b>harbor-mutual</b>.example</div>
</section>

</body>
</html>
```